Coffee Package Design

We need a new package design for a coffee company. Need to be a mix between modern and classic design combined together. We are open to different ideas.
We changing our product name from Café Verlona to Café Rostelli. The picture upload
shows what the product looks like. We want something completely different. The name of the company should go on the back of the package.
Updates

Hello Everyone,

Please read description, we are going with a new name and design for the product.

Café Rostelli. Café Verlona is what we are replacing with Café Rostelli, we are looking for new

look and design, please submit new designs.

There is a change in the description. Please take out Premium coffee blend and replace with Italian Roast.                                    

Industry/Entity Type

Cafe

Requirements
Must have
• You can use up to 6 colors.
Please put these items on design: Café Rostelli (this is the product name), Regular Premium Blend Coffee, 100% Arabica,
Dumbrell & Sons (name of the company), Tyler, TX on the back of the package

The file uploaded is an example of one of our products and how the package film
is sized.

```html
<!DOCTYPE html>
<html lang="en">
<head>
<meta charset="utf-8">
<title>Café Rostelli – Package Film</title>
<link rel="stylesheet" href="https://fonts.googleapis.com/css2?family=Bebas+Neue&family=Questrial&display=swap">
<style>
  :root {
    --page: #ffffff;
    --film: #3f3434;
    --seam: #332626;
    --panel: rgba(255, 255, 255, 0.08);
    --ink-light: #d9dcdc;
    --ink-white: #f4f1ee;
    --accent: #e03a26;
  }
  html, body {
    margin: 0;
    width: 1200px;
    height: 750px;
    overflow: hidden;
    background: var(--page);
  }
  .package-film {
    position: absolute;
    left: 39px;
    top: 36px;
    width: 792px;
    height: 459px;
    background: var(--film);
  }
  .film-texture {
    position: absolute;
    left: 0;
    top: 0;
    width: 729px;
    height: 459px;
    background: radial-gradient(circle at 50% 50%, #463a3a 0%, var(--film) 70%);
  }
  .seal-strip {
    position: absolute;
    right: 0;
    top: 0;
    width: 63px;
    height: 459px;
    background: var(--seam);
  }
  .panel {
    position: absolute;
    top: 54px;
    height: 370px;
    background: var(--panel);
  }
  .panel--side-left { left: 71px; width: 136px; }
  .panel--front { left: 228px; width: 336px; }
  .panel--back { left: 584px; width: 136px; }

  .product-name {
    font-family: "Bebas Neue", sans-serif;
    color: var(--ink-light);
    margin: 0;
    line-height: 0.9;
    font-weight: 400;
  }
  .product-name__line { display: block; }
  .accent-square {
    display: inline-block;
    background: var(--accent);
    vertical-align: middle;
  }

  .front-name {
    position: absolute;
    left: 38px;
    top: 48px;
  }
  .front-name .product-name__line--small { font-size: 62px; }
  .front-name .product-name__line--large { font-size: 96px; }
  .front-name .accent-square { width: 16px; height: 16px; margin-left: 10px; margin-top: -10px; }

  .front-details {
    position: absolute;
    left: 38px;
    top: 300px;
    color: var(--ink-white);
  }
  .front-details__claim {
    margin: 0;
    font-family: "Bebas Neue", sans-serif;
    font-size: 19px;
    line-height: 17px;
  }
  .front-details__variant {
    margin: 2px 0 0;
    font-family: "Questrial", sans-serif;
    font-size: 15px;
  }

  .side-name {
    position: absolute;
    left: 68px;
    top: 185px;
    transform: translate(-50%, -50%) rotate(90deg);
    white-space: nowrap;
  }
  .side-name .product-name { font-size: 40px; }
  .side-name .accent-square { width: 10px; height: 10px; margin-left: 8px; }

  .maker {
    position: absolute;
    left: 68px;
    top: 185px;
    transform: translate(-50%, -50%) rotate(-90deg);
    white-space: nowrap;
    font-family: "Bebas Neue", sans-serif;
    color: var(--ink-light);
    font-size: 24px;
    line-height: 21px;
    letter-spacing: 1px;
    text-align: center;
  }
  .maker p { margin: 0; }
</style>
</head>
<body>
  <main class="package-film">
    <div class="film-texture" role="img" aria-label="Subtle dark brown repeating floral rosette pattern across the film"></div>
    <div class="seal-strip"></div>

    <section class="panel panel--side-left">
      <div class="side-name">
        <p class="product-name">Café Rostelli<span class="accent-square"></span></p>
      </div>
    </section>

    <section class="panel panel--front">
      <div class="front-name">
        <h1 class="product-name">
          <span class="product-name__line product-name__line--small">Café<span class="accent-square"></span></span>
          <span class="product-name__line product-name__line--large">Rostelli</span>
        </h1>
      </div>
      <div class="front-details">
        <p class="front-details__claim">100% Arabica</p>
        <p class="front-details__claim">Premium Blend Coffee</p>
        <p class="front-details__variant">Regular</p>
      </div>
    </section>

    <section class="panel panel--back">
      <div class="maker">
        <p>Dumbrell &amp; Sons</p>
        <p>Marlow, Texas</p>
      </div>
    </section>
  </main>
</body>
</html>
```